Talvey Vineyards Plinkr website

We are opening a new winery called Talvey Vineyards. We think that "Wine should be an experience..." To aid in that experience, each bottle of wine label will have a unique QR code that directs patrons to a page on the site that highlights the wines. On this page each wine bottle will be displayed, the winemaking notes will be included. Also included will be food pairings with recipes, movie and music ideas and anything else that will add to the experience. I need a website that helps showcase annual wines, has a members only area (for the wine club) and allows people to purchase wine on-line. I've started the beginning of a site on Plinkr - talveyvineyards.example. There's no requirement or expectation to simply finish what I've started. I just needed to get something up and live. Let your imagination take over. I want to unique site and kicks a*s...

Logo font is Trajan Pro...

I'm open to any designs, meaning don't feel like you have to complete what I started.

I want to keep the logo and the font, however...

Other fonts used should compliment Trajan Pro.

Serif
• Trajan Pro is what was used for the logo

• Attractive and compelling home page, red wine section, white wine section, members only area, page that speaks of and allows purchase into a wine club, all easy enough for me to edit and add pages without coding knowledge. Adding pages is why I chose Plinkr as the platform. Here is a list of the pages or tabs: About, Events, Harvest Circle, Press/Accolades, Wines - Red/White/Dessert/Summer Series (as sub pages), Contact

```html
<!DOCTYPE html>
<html lang="en">
<head>
<meta charset="utf-8">
<title>Talvey Vineyards</title>
<link href="https://fonts.googleapis.com/css2?family=Cinzel:wght@400;500&family=Arimo:wght@400;700&display=swap" rel="stylesheet">
<style>
:root{
  --ink:#07080a;
  --panel:#0b0c0e;
  --white:#ffffff;
  --gold:#c9a94a;
  --gold-deep:#5e4f12;
  --amber:#c7781c;
  --amber-dim:#8a5a1e;
  --label:#8c8c8c;
  --rule:#3a3a3a;
}
*{margin:0;padding:0;box-sizing:border-box}
html,body{width:1171px;height:1200px;overflow:hidden;background:var(--ink)}
body{position:relative;font-family:"Cinzel",serif;color:var(--white)}
.abs{position:absolute}
/* header */
.header{left:0;top:0;width:1171px;height:66px;background:var(--ink)}
.brand-box{border:1px solid #555;border-radius:4px;display:flex;align-items:center;justify-content:center;text-align:center;font-family:"Cinzel",serif;color:var(--white);line-height:1.15}
.header .brand-box{left:88px;top:8px;width:46px;height:48px;font-size:7px}
.nav a{position:absolute;top:40px;font-family:"Arimo",sans-serif;font-weight:700;font-size:10px;color:var(--white);text-decoration:none;white-space:nowrap}
.pill{top:8px;height:18px;border:1px solid #bbb;border-radius:2px;font-family:"Arimo",sans-serif;font-size:8px;display:flex;align-items:center;gap:5px;padding-left:8px;white-space:nowrap;overflow:hidden}
.pill.phone{left:856px;width:104px;background:var(--white);color:#111}
.pill.mail{left:977px;width:111px;color:#ddd}
.pill svg{width:8px;height:8px;flex:none}
/* hero */
.hero{left:0;top:66px;width:1171px;height:290px}
.hero-photo{left:2px;top:0;width:1169px;height:290px;background:radial-gradient(ellipse 30% 60% at 54% 35%,#a87a2a 0%,#5a3a12 40%,transparent 70%),linear-gradient(180deg,#4a3a24 0%,#2a2016 35%,#6a4a1c 60%,#1a140c 100%)}
.hero-curve{left:0;top:200px;width:1171px;height:92px}
.hero-copy{left:0;top:108px;width:1171px;text-align:center}
.hero-copy .kicker{font-size:24px;line-height:1.2;color:var(--white)}
.hero-copy h1{font-weight:500;font-size:40px;color:var(--gold);line-height:1.05;letter-spacing:1px}
.hero-copy p{width:560px;margin:8px auto 0;font-size:11px;line-height:1.2;color:#f2e8d2}
.btn-read{left:504px;top:297px;width:142px;height:27px;background:#0b0a08;border:1px solid #3c2e12;color:var(--gold);font-size:11px;display:flex;align-items:center;justify-content:center}
/* winemaker */
.rule-top{left:66px;top:366px;width:452px;height:1px;background:#555}
.portrait{left:66px;top:382px;width:428px;height:206px;background:radial-gradient(ellipse 50% 70% at 55% 45%,#9a9a9a 0%,#555 45%,var(--ink) 80%)}
.message{left:585px;top:382px;width:586px;height:218px;background:var(--panel);padding:78px 64px 0 66px}
.message h2{font-weight:400;font-size:26px;line-height:1.1;color:var(--amber);white-space:nowrap}
.message p{font-size:9px;line-height:1.2;color:var(--amber-dim);margin-top:6px}
/* contact */
.contact-info{left:150px;top:741px;width:350px;text-align:center;font-size:12px}
.contact-info .brand-box{width:100px;height:78px;margin:0 auto 14px;font-size:12px}
.contact-info div.line{height:24px;display:flex;align-items:center;justify-content:center;gap:5px}
.contact-info svg{width:10px;height:10px;fill:var(--white)}
.divider{left:584px;top:680px;width:1px;height:303px;background:#555}
.contact-title{left:620px;top:676px;width:400px;text-align:center;font-size:19px}
.field-label{left:610px;font-size:11px;color:var(--label)}
.field{left:718px;width:352px;background:var(--white);border-radius:2px;color:#8a8a8a;font-size:11px;padding:0 8px;display:flex;align-items:center}
.field.select{color:#111;justify-content:space-between}
.field.area{align-items:flex-start;padding-top:10px}
.btn-submit{left:718px;top:965px;width:167px;height:18px;background:var(--gold-deep);color:#000;font-size:11px;display:flex;align-items:center;justify-content:center}
/* footer */
.footer .brand-box{left:151px;top:1078px;width:167px;height:118px;border-width:1.5px;font-size:17px}
.footer h3{font-weight:400;color:var(--white)}
.foot-address{left:464px;top:1080px;width:170px}
.foot-address h3{font-size:18px;margin-bottom:12px}
.foot-address div{font-size:6.5px;line-height:1.3;margin-bottom:10px;display:flex;gap:5px}
.foot-address svg{width:7px;height:7px;fill:var(--white);flex:none}
.foot-menu{left:705px;top:1080px}
.foot-menu h3{font-size:12px;margin-bottom:12px}
.foot-menu a{display:block;font-size:8px;color:var(--white);text-decoration:none;margin-bottom:6px}
.foot-social{left:946px;top:1080px}
.foot-social h3{font-size:18px;line-height:1.1}
.circles{display:flex;gap:10px;margin-top:18px}
.circles span{width:18px;height:18px;border-radius:50%;background:var(--white)}
</style>
</head>
<body>

<header class="abs header">
  <div class="abs brand-box">Talvey<br>Vineyards</div>
  <nav class="nav">
    <a style="left:289px" href="#">About Us</a>
    <a style="left:394px" href="#">Services</a>
    <a style="left:497px" href="#">Products</a>
    <a style="left:601px" href="#">Gallery</a>
    <a style="left:706px" href="#">Testimonial</a>
    <a style="left:809px" href="#">Contact Us</a>
  </nav>
  <div class="abs pill phone"><svg viewBox="0 0 10 10"><path d="M2 0.5 L3.6 2.6 L2.8 3.6 Q4 6 6.4 7.2 L7.4 6.4 L9.5 8 L8.4 9.5 Q3.5 9 0.5 1.6 Z" fill="#111"/></svg>+100 2222 3333</div>
  <div class="abs pill mail"><svg viewBox="0 0 10 8"><rect width="10" height="8" fill="#ddd"/><path d="M0 0 L5 4.5 L10 0" stroke="#07080a" fill="none"/></svg>hi@talvey.example</div>
</header>

<section class="abs hero">
  <div class="abs hero-photo" role="img" aria-label="Photo of a glass of white wine on a wooden bar table with blurred warm lights"></div>
  <svg class="abs hero-curve" viewBox="0 0 1171 92" preserveAspectRatio="none">
    <defs><linearGradient id="goldline" x1="0" x2="1"><stop offset="0" stop-color="#3a2a0a"/><stop offset=".6" stop-color="#6a4e12"/><stop offset="1" stop-color="#d8b040"/></linearGradient></defs>
    <path d="M0 92 L0 66 Q300 100 620 60 Q900 20 1171 10 L1171 92 Z" fill="var(--ink)"/>
    <path d="M0 66 Q300 100 620 60 Q900 20 1171 10" stroke="url(#goldline)" stroke-width="3" fill="none"/>
  </svg>
  <div class="abs hero-copy">
    <div class="kicker">Welcome to</div>
    <h1>Talvey Vineyards</h1>
    <p>We believe that everyone deserves to have great tasting and high quality wine. That is why after more than 10 years of experience, we decided to open an online store.</p>
  </div>
</section>
<div class="abs btn-read">Read more</div>

<div class="abs rule-top"></div>
<div class="abs portrait" role="img" aria-label="Black and white photo of the winemaker tasting a glass of wine"></div>
<section class="abs message">
  <h2>A message from the winemaker</h2>
  <p>I started my winemaking journey with one simple goal in mind - I wanted to make wine as good or better than the wine I could buy. At the time of that goal in 2015, I had no perspective on the path that would form before me.<br>
  I'm excited for you to try my wine. Pair it with the food ideas. Follow the recipes; listen to the music.<br>
  Enjoy...the experience.<br>
  --Edwin Talvey--</p>
</section>

<section class="abs contact-info">
  <div class="brand-box">Talvey<br>Vineyards</div>
  <div class="line"><svg viewBox="0 0 10 10"><path d="M2 0.5 L3.6 2.6 L2.8 3.6 Q4 6 6.4 7.2 L7.4 6.4 L9.5 8 L8.4 9.5 Q3.5 9 0.5 1.6 Z"/></svg>+100 222 333</div>
  <div class="line"><svg viewBox="0 0 10 8"><rect width="10" height="8"/><path d="M0 0 L5 4.5 L10 0" stroke="#07080a" fill="none"/></svg>hi@talvey.example</div>
  <div class="line">Harbour Lane, Cove Point 2100, Australia</div>
  <div class="line">PO Box 208: Ridgeford 5300, Australia</div>
</section>

<div class="abs divider"></div>
<div class="abs contact-title">Contact Us</div>
<div class="abs field-label" style="top:720px">First Name</div>
<div class="abs field" style="top:712px;height:29px">Your name..</div>
<div class="abs field-label" style="top:762px">Last Name</div>
<div class="abs field" style="top:755px;height:29px">Your last name..</div>
<div class="abs field-label" style="top:802px">Country</div>
<div class="abs field select" style="top:798px;height:25px">Australia<svg width="8" height="6" viewBox="0 0 8 6"><path d="M1 1 L4 4.5 L7 1" stroke="#111" stroke-width="1.5" fill="none"/></svg></div>
<div class="abs field-label" style="top:898px">Subject</div>
<div class="abs field area" style="top:837px;height:118px">Write something..</div>
<div class="abs btn-submit">Submit</div>

<footer class="footer">
  <div class="abs brand-box">Talvey<br>Vineyards</div>
  <div class="abs foot-address">
    <h3>Address</h3>
    <div><svg viewBox="0 0 10 10"><path d="M2 0.5 L3.6 2.6 L2.8 3.6 Q4 6 6.4 7.2 L7.4 6.4 L9.5 8 L8.4 9.5 Q3.5 9 0.5 1.6 Z"/></svg>+100 222 333</div>
    <div><svg viewBox="0 0 10 8"><rect width="10" height="8"/><path d="M0 0 L5 4.5 L10 0" stroke="#07080a" fill="none"/></svg>hi@talvey.example</div>
    <div>Harbour Lane, Cove Point 2100,<br>Australia</div>
    <div>PO Box 208: Ridgeford 5300,<br>Australia</div>
  </div>
  <nav class="abs foot-menu">
    <h3>Menu</h3>
    <a href="#">About Us</a>
    <a href="#">Services</a>
    <a href="#">Products</a>
    <a href="#">Gallery</a>
    <a href="#">Contact Us</a>
  </nav>
  <div class="abs foot-social">
    <h3>Social<br>Media</h3>
    <div class="circles">
      <span role="img" aria-label="Social profile one"></span>
      <span role="img" aria-label="Social profile two"></span>
      <span role="img" aria-label="Social profile three"></span>
    </div>
  </div>
</footer>

</body>
</html>
```